Business Card for a Dental Office

The design should communicate integrity, quality and reliability. We also want the card look elegant, simple, but still stand out, different from the traditional-dental-office business card.

Business

```html
<!DOCTYPE html>
<html lang="en">
<head>
<meta charset="UTF-8">
<title>Harwell Dental Studio – Business Card</title>
<link href="https://fonts.googleapis.com/css2?family=Oswald:wght@600&family=Arimo:wght@400;700&display=swap" rel="stylesheet">
<style>
  :root {
    --stage: #3a3a3c;
    --gold: #d9b21a;
    --gold-light: #f5e04a;
    --gold-deep: #b48d0f;
    --ink: #111111;
    --paper: #ffffff;
    --white-text: #f2f2f2;
    --rule: #6b6b6b;
  }
  * { box-sizing: border-box; margin: 0; padding: 0; }
  html, body {
    width: 1200px; height: 950px; overflow: hidden;
    background: var(--stage);
    font-family: "Arimo", Arial, sans-serif;
  }
  .canvas { position: relative; width: 1200px; height: 950px; }

  .card {
    position: absolute; width: 700px; height: 400px;
    box-shadow: 0 18px 40px rgba(0,0,0,.45);
    overflow: hidden;
  }

  /* Back side */
  .card-back {
    left: 80px; top: 60px;
    background: radial-gradient(ellipse at 50% 40%, var(--gold-light) 0%, var(--gold) 45%, var(--gold-deep) 100%);
    display: flex; flex-direction: column; align-items: center; justify-content: center;
  }
  .back-brand { display: flex; align-items: center; gap: 14px; }
  .brand-mark { width: 30px; height: 30px; background: var(--ink); }
  .back-brand .brand-name {
    font-family: "Oswald", "Arial Narrow", sans-serif; font-weight: 600;
    font-size: 38px; letter-spacing: 1px; color: var(--ink); text-transform: uppercase;
  }
  .back-web {
    margin-top: 70px; font-size: 16px; letter-spacing: 4px; color: var(--ink);
  }

  /* Front side */
  .card-front { left: 420px; top: 480px; background: var(--paper); }
  .front-top {
    height: 205px; display: flex; align-items: center; padding-left: 95px;
  }
  .front-brand .brand-row { display: flex; align-items: center; gap: 12px; }
  .front-brand .brand-mark { width: 26px; height: 26px; background: var(--ink); }
  .front-brand .brand-name {
    font-family: "Oswald", "Arial Narrow", sans-serif; font-weight: 600;
    font-size: 34px; color: var(--ink); text-transform: uppercase; letter-spacing: .5px;
  }
  .tagline {
    margin: 4px 0 0 38px; font-size: 13px; font-weight: 700;
    color: var(--gold); text-transform: uppercase; letter-spacing: .6px;
  }
  .gold-rule { height: 5px; background: var(--gold); }
  .front-bottom {
    height: 190px; background: linear-gradient(160deg, #262626 0%, var(--ink) 55%, #000 100%);
    display: flex; align-items: center; padding: 0 40px;
  }
  .holder {
    width: 300px; text-align: right; padding-right: 26px; color: var(--white-text);
    font-size: 17px; line-height: 1.45;
  }
  .holder-name { color: var(--gold); font-size: 20px; }
  .divider { width: 1px; height: 120px; background: var(--rule); }
  .contacts { list-style: none; padding-left: 24px; color: var(--white-text); font-size: 17px; }
  .contacts li { display: flex; align-items: center; gap: 10px; line-height: 1.6; }
  .contacts svg { width: 16px; height: 16px; fill: var(--gold); flex: none; }
</style>
</head>
<body>
<main class="canvas">

  <section class="card card-back" aria-label="Card back">
    <div class="back-brand">
      <span class="brand-mark"></span>
      <span class="brand-name">Harwell Dental Studio</span>
    </div>
    <p class="back-web">www.harwelldental.com</p>
  </section>

  <section class="card card-front" aria-label="Card front">
    <div class="front-top">
      <div class="front-brand">
        <div class="brand-row">
          <span class="brand-mark"></span>
          <span class="brand-name">Harwell Dental Studio</span>
        </div>
        <p class="tagline">Your smile is your gift to others</p>
      </div>
    </div>
    <div class="gold-rule"></div>
    <div class="front-bottom">
      <div class="holder">
        <p class="holder-name">Marcus Hale</p>
        <p>President</p>
        <p>2718 Linden Grove Road</p>
        <p>Maple Hollow, NY 12045</p>
      </div>
      <div class="divider"></div>
      <ul class="contacts">
        <li>
          <svg viewBox="0 0 16 16"><path d="M2 5c0-2 2-3 6-3s6 1 6 3l-3 1-1-2H6L5 6 2 5zM4 7h8l2 7H2l2-7zm4 2a2 2 0 100 4 2 2 0 000-4z"/></svg>
          555 0142 7781
        </li>
        <li>
          <svg viewBox="0 0 16 16"><path d="M4 1h8v14H4zM5.5 3v9h5V3zM7 13h2v1H7z"/></svg>
          555 0193 4420
        </li>
        <li>
          <svg viewBox="0 0 16 16"><path d="M4 1h8v4H4zM2 6h12v6h-2v3H4v-3H2zM5 10v4h6v-4z"/></svg>
          555 0167 2309
        </li>
        <li>
          <svg viewBox="0 0 16 16"><path d="M1 3h14v10H1zm1.5 1.5L8 9l5.5-4.5z"/></svg>
          marcus@harwelldental.com
        </li>
      </ul>
    </div>
  </section>

</main>
</body>
</html>
```